Business card design for engineering firm specializing in defense industry.

We need a professional business card design. Something simple but stands out. We are an engineering company specializing in composites in the defense industry.
Industry/Entity Type
Defense
Contact Information for Business Card
A simple black business card with the Varlonix yellow color is what we had in mind but open for other designs.
Colors
ffc214

```html
<!DOCTYPE html>
<html lang="en">
<head>
<meta charset="utf-8">
<title>Varlonix Business Card</title>
<link href="https://fonts.googleapis.com/css2?family=Roboto:wght@300;400;700&display=swap" rel="stylesheet">
<style>
  :root {
    --brand-yellow: #ffc214;
    --ink: #000000;
    --paper: #ffffff;
    --backdrop: #e4e4e4;
    --muted: #555555;
    --card-dark: #141414;
    --card-dark-soft: #262626;
  }
  * { margin: 0; padding: 0; box-sizing: border-box; }
  html, body {
    width: 1125px; height: 1200px; overflow: hidden;
    background: var(--backdrop);
    font-family: "Roboto", Arial, sans-serif;
  }
  .canvas { position: relative; width: 1125px; height: 1200px; }
  .card {
    position: absolute; left: 150px; width: 826px; height: 471px; overflow: hidden;
  }
  .card-front { top: 98px; background: var(--paper); }
  .card-back { top: 631px; background: var(--card-dark); }

  .holder { position: absolute; left: 62px; top: 52px; }
  .holder-name {
    font-size: 35px; font-weight: 400; color: var(--ink); letter-spacing: 0.5px; line-height: 1;
  }
  .holder-title {
    margin-top: 6px; font-size: 22px; font-weight: 400; color: var(--brand-yellow);
    letter-spacing: 0.5px; line-height: 1;
  }

  .contact-band {
    position: absolute; left: 0; top: 151px; width: 542px; height: 211px; background: var(--ink);
  }
  .contact-list { position: absolute; left: 65px; top: 40px; list-style: none; }
  .contact-item {
    display: flex; align-items: center; height: 26.3px;
    color: var(--paper); font-size: 19px; font-weight: 300;
  }
  .contact-icon { width: 20px; height: 20px; margin-right: 12px; flex: none; }
  .contact-icon * { fill: var(--brand-yellow); }

  .accent-block {
    position: absolute; left: 755px; top: 151px; width: 71px; height: 211px; background: var(--brand-yellow);
  }

  .address {
    position: absolute; left: 62px; top: 400px;
    font-size: 19px; font-weight: 300; color: var(--muted);
  }

  .back-texture {
    position: absolute; inset: 0;
    background: radial-gradient(ellipse at 50% 45%, var(--card-dark-soft) 0%, var(--card-dark) 75%);
  }
  .brand-lockup {
    position: absolute; left: 50%; top: 50%; transform: translate(-50%, -50%);
    display: flex; align-items: center; gap: 18px;
  }
  .brand-square { width: 48px; height: 48px; background: var(--brand-yellow); }
  .brand-name {
    font-size: 72px; font-weight: 700; color: var(--paper); line-height: 1; letter-spacing: 1px;
  }
</style>
</head>
<body>
<div class="canvas">
  <section class="card card-front">
    <div class="holder">
      <div class="holder-name">DANIEL MERCER</div>
      <div class="holder-title">FOUNDER</div>
    </div>

    <div class="contact-band">
      <ul class="contact-list">
        <li class="contact-item">
          <svg class="contact-icon" viewBox="0 0 20 20"><path d="M4 2l3 0 2 4-2 2c1 2 3 4 5 5l2-2 4 2v3c0 1-1 2-2 2C8 18 2 12 2 4c0-1 1-2 2-2z"/></svg>
          555 214 7730
        </li>
        <li class="contact-item">
          <svg class="contact-icon" viewBox="0 0 20 20"><path d="M6 1h8a1 1 0 0 1 1 1v16a1 1 0 0 1-1 1H6a1 1 0 0 1-1-1V2a1 1 0 0 1 1-1zm1 3v11h6V4zm3 12.5a1 1 0 1 0 0 .01z"/></svg>
          555 390 6148
        </li>
        <li class="contact-item">
          <svg class="contact-icon" viewBox="0 0 20 20"><path d="M5 2h8l2 2v4H5zM2 9h16v6h-3v3H5v-3H2zm4 4v3h8v-3z"/></svg>
          555 782 4051
        </li>
        <li class="contact-item">
          <svg class="contact-icon" viewBox="0 0 20 20"><path d="M2 5h16v1l-8 5-8-5zm0 3l8 5 8-5v7H2z"/></svg>
          daniel@varlonix.com
        </li>
        <li class="contact-item">
          <svg class="contact-icon" viewBox="0 0 20 20"><path d="M10 1a9 9 0 1 1 0 18 9 9 0 0 1 0-18zm-3 4c-1 1-3 3-2 5 1 1 3 0 3 2s1 3 2 4c1-2 0-3 1-4 1-2-1-3-3-3 0-2 2-2 1-4zm6 0c-1 1 0 2 1 3 1 0 2-1 1-2z"/></svg>
          www.varlonix.com
        </li>
      </ul>
    </div>

    <div class="accent-block"></div>

    <p class="address">4120 Ridgeway Court, Fairbanks, Alaska 99701</p>
  </section>

  <section class="card card-back">
    <div class="back-texture" role="img" aria-label="Faint repeating geometric pattern across the dark card"></div>
    <div class="brand-lockup">
      <div class="brand-square"></div>
      <div class="brand-name">Varlonix</div>
    </div>
  </section>
</div>
</body>
</html>
```